Business Card Design for a Personal Trainer

I need a business card design for my job as a personal trainer. It should have a unique, modern and exclusive design. On the front there should be only my logo with my name and my job. 0163/2918374 Tobias Kellinger Lindenfeldweg 14 80412 Munich Germany The most important contact information is the web adress. it can be bigger than the rest, but its not necessary. The card should be 8,5cmx5,5cm big. Font: Roboto. Colors: black, white, gray, 56c1ff.

```html
<!DOCTYPE html>
<html lang="de">
<head>
<meta charset="utf-8">
<title>Tobias Kellinger – Personal Trainer</title>
<link href="https://fonts.googleapis.com/css2?family=Roboto:wght@400;500&display=swap" rel="stylesheet">
<style>
  :root {
    --accent: #56c1ff;
    --text-grey: #c9cdd1;
    --bg-center: #1f3b4f;
    --bg-mid: #142838;
    --bg-edge: #070d13;
    --photo-light: #7a7d80;
    --photo-dark: #2a2c2e;
  }
  html, body {
    margin: 0;
    padding: 0;
    width: 1200px;
    height: 777px;
    overflow: hidden;
    background: #0a1118;
  }
  .card {
    position: relative;
    width: 1200px;
    height: 777px;
    overflow: hidden;
    font-family: "Roboto", sans-serif;
    background: radial-gradient(ellipse 70% 65% at 48% 50%, var(--bg-center) 0%, var(--bg-mid) 55%, var(--bg-edge) 100%);
  }
  .contact {
    position: absolute;
    right: 696px;
    top: 0;
    text-align: right;
    white-space: nowrap;
  }
  .contact p { margin: 0; position: absolute; right: 0; }
  .name {
    top: 228px;
    font-size: 50px;
    color: var(--accent);
  }
  .role {
    top: 286px;
    font-size: 22px;
    color: var(--text-grey);
  }
  .phone {
    top: 333px;
    font-size: 49px;
    color: var(--accent);
  }
  .address-street, .address-city, .email, .web {
    font-size: 29px;
    color: var(--text-grey);
  }
  .address-street { top: 392px; }
  .address-city { top: 433px; }
  .email { top: 489px; }
  .web { top: 526px; }
  .divider {
    position: absolute;
    left: 597px;
    top: 221px;
    width: 6px;
    height: 344px;
    background: var(--accent);
  }
  .portrait {
    position: absolute;
    left: 705px;
    top: 74px;
    width: 410px;
    height: 703px;
    border-radius: 160px 160px 0 0;
    background: linear-gradient(180deg, var(--photo-light) 0%, #4a4c4f 35%, var(--photo-dark) 100%);
  }
</style>
</head>
<body>
  <main class="card">
    <section class="contact">
      <p class="name">Tobias Kellinger</p>
      <p class="role">Personal Trainer</p>
      <p class="phone">0163 2918 - 374</p>
      <p class="address-street">Lindenfeldweg 14</p>
      <p class="address-city">80412 München</p>
      <p class="email">t.kellinger@mailpost.de</p>
      <p class="web">www.tobiaskellinger.de</p>
    </section>
    <div class="divider"></div>
    <div class="portrait" role="img" aria-label="Black and white photo of the trainer standing with crossed arms in a fitted long-sleeve shirt"></div>
  </main>
</body>
</html>
```